Tallowreed Consulting Schedule Of Rates

We need a brochure / proposal for our new company. Our company is a start up based in Australia who provides engineering and sales support to other renewable energy companies. Our brochure is a pitch-deck / sales item that catalogues our key services. We are engineering consultants.

Our website is www.tallowreedpartners.com.au. Please review the website to get a feel of colour schemes etc.

We are looking for a strong, trustworthy feel, but the brochure also needs to be sales driven and to the point.

The second page that contains the $30 price point needs to be loud and clear.

The use of relevant icons throughout the document will be viewed favorably.

Please format the tables to look attractive.

The document will need to be in an editable format so content can be edited by us at a later date.

Please feel free to use the pics within the attached word document. The winning design will be provided with updated, clearer images upon request.

Thank you

Target Market(s)

Businesses that either sell or install solar PV and other renewable energy systems in Australia. Most of target market are likely to be electrical contractors.

Industry/Entity Type

Engineering

Colors
0255a3
0492cd
ffffff

Requirements
Must have
• Icons, graphics presentation, Clean and Clear, Business oriented. Sharp sales feel
Nice to have
• solar picture backgrounds maybe
Should not have
• cartoons, over sales driven,

```html
<!DOCTYPE html>
<html lang="en">
<head>
<meta charset="utf-8">
<title>Tallowreed Consulting – Schedule of Rates</title>
<link href="https://fonts.googleapis.com/css2?family=Roboto+Condensed:wght@400;700&display=swap" rel="stylesheet">
<style>
  :root{
    --navy:#0255a3;
    --deep:#0a3f86;
    --sky:#0492cd;
    --white:#ffffff;
    --ink:#1b2a3a;
    --stage:#e4e9ee;
    --mist:#dfe8f2;
  }
  *{box-sizing:border-box;margin:0;padding:0}
  html,body{width:1200px;height:708px;overflow:hidden}
  body{background:var(--stage);font-family:"Roboto Condensed",Arial,sans-serif;color:var(--ink);position:relative}
  .page{position:absolute;width:380px;height:537px;overflow:hidden;box-shadow:0 6px 18px rgba(0,0,0,.18)}
  .page svg.bg{position:absolute;inset:0;width:100%;height:100%}
  .cover{left:20px;top:85px;background:var(--white)}
  .spread-left{left:420px;top:85px}
  .spread-right{left:800px;top:85px}

  /* cover */
  .brand{position:absolute;top:30px;left:0;width:100%;text-align:center;display:flex;justify-content:center;align-items:center;gap:8px}
  .brand-dot{width:12px;height:12px;border-radius:50%;background:var(--navy)}
  .brand-name{font-size:26px;font-weight:700;color:var(--ink);letter-spacing:-.3px}
  .cover-title{position:absolute;top:138px;left:0;width:100%;text-align:center;color:var(--white);font-weight:700;font-size:40px;line-height:40px;text-shadow:0 2px 4px rgba(0,40,90,.5)}
  .cover-title .amp{font-size:24px}
  .cover-sub{position:absolute;top:232px;left:0;width:100%;text-align:center;font-size:17px;line-height:20px;color:var(--ink)}
  .contact{position:absolute;right:16px;bottom:18px;text-align:right;font-size:10px;line-height:13px;color:var(--ink)}

  /* spread left */
  .price-badge{position:absolute;border-radius:50%;background:var(--white);border:4px solid var(--deep);text-align:center;color:var(--ink);display:flex;flex-direction:column;justify-content:center;align-items:center;padding:10px}
  .badge-30{left:14px;top:100px;width:126px;height:126px;font-size:12px;line-height:14px}
  .badge-30 .big{font-size:34px;line-height:36px;font-weight:700;color:var(--navy)}
  .badge-30 .big small{font-size:13px;color:var(--ink);font-weight:400}
  .badge-3d{left:258px;top:360px;width:114px;height:114px;font-size:11px;line-height:13px}
  .badge-3d .big{font-size:24px;line-height:24px;font-weight:700;color:var(--navy)}
  .tier{position:absolute;background:var(--navy);color:var(--white);font-weight:700;font-size:10.5px;line-height:12px;text-align:center;padding:7px 10px}
  .tier-mid{right:0;top:190px;width:150px}
  .tier-large{left:0;top:360px;width:160px}
  .service-head{position:absolute;top:268px;left:0;width:100%;text-align:center}
  .service-head h2{color:var(--navy);font-size:17px;font-weight:700;margin-bottom:6px}
  .service-head p{font-size:10px;line-height:12px}

  /* spread right */
  .grid-title{position:absolute;right:14px;top:36px;text-align:right;color:var(--white);font-weight:700;font-size:19px;line-height:19px}
  .rate-card{position:absolute;background:var(--navy);color:var(--white);box-shadow:0 3px 6px rgba(0,30,70,.35)}
  .rate-card h3{background:var(--sky);font-size:11px;text-align:center;padding:3px 0;font-weight:700}
  .rate-card table{width:100%;border-collapse:collapse;font-size:6.6px;line-height:8px}
  .rate-card th,.rate-card td{border:1px solid rgba(255,255,255,.75);padding:0 3px;text-align:left;vertical-align:top;font-weight:400}
  .rate-card th{font-weight:700}
  .rate-card .rate{text-align:right;width:26px}
  .card-a{left:70px;top:140px;width:245px}
  .card-b{left:42px;top:258px;width:240px}
  .card-c{left:20px;top:388px;width:232px}
</style>
</head>
<body>

<section class="page cover">
  <svg class="bg" viewBox="0 0 380 537" preserveAspectRatio="none">
    <defs>
      <linearGradient id="skyFill" x1="0" y1="0" x2="0" y2="1">
        <stop offset="0" stop-color="#3f82c8"/><stop offset=".6" stop-color="#a9cbe8"/><stop offset="1" stop-color="#d6e6f3"/>
      </linearGradient>
      <linearGradient id="panelFill" x1="0" y1="0" x2="1" y2="1">
        <stop offset="0" stop-color="#2a4f9e"/><stop offset="1" stop-color="#10306f"/>
      </linearGradient>
    </defs>
    <g role="img" aria-label="Photo of blue sky with white clouds">
      <rect x="0" y="40" width="380" height="300" fill="url(#skyFill)"/>
    </g>
    <g role="img" aria-label="Photo of rows of solar panels">
      <path d="M0 300 Q190 300 380 285 L380 470 L0 470 Z" fill="url(#panelFill)"/>
    </g>
    <path d="M0 0 L380 0 L380 20 Q330 120 190 120 Q60 120 15 30 L0 30 Z" fill="var(--white)"/>
    <path d="M12 28 Q60 126 190 126 Q330 126 380 16" fill="none" stroke="var(--navy)" stroke-width="5"/>
    <path d="M0 470 Q200 470 380 330 L380 420 Q250 500 0 500 Z" fill="var(--sky)"/>
    <path d="M0 440 Q220 450 380 300 L380 340 Q220 470 0 470 Z" fill="var(--navy)"/>
    <path d="M0 500 Q250 500 380 420 L380 537 L0 537 Z" fill="#e9edf1"/>
    <path d="M0 500 Q250 500 380 420" fill="none" stroke="var(--deep)" stroke-width="6"/>
  </svg>
  <div class="brand"><span class="brand-dot"></span><span class="brand-name">Tallowreed Consulting</span></div>
  <h1 class="cover-title">Design <span class="amp">&amp;</span> Support<br>Services</h1>
  <p class="cover-sub">Schedule of Rates<br>Grid and Off Grid<br>5kW – 10MW</p>
  <p class="contact">03 9410 2736 &nbsp;|&nbsp; 0412 683 905<br>sales@tallowreedpartners.com.au<br>www.tallowreedpartners.com.au</p>
</section>

<section class="page spread-left">
  <svg class="bg" viewBox="0 0 380 537" preserveAspectRatio="none">
    <defs>
      <linearGradient id="roofTop" x1="0" y1="0" x2="0" y2="1">
        <stop offset="0" stop-color="#8c9aa6"/><stop offset=".75" stop-color="#d3dbe2"/><stop offset="1" stop-color="#ffffff"/>
      </linearGradient>
      <linearGradient id="roofLow" x1="0" y1="0" x2="0" y2="1">
        <stop offset="0" stop-color="#e9eef2"/><stop offset=".35" stop-color="#a5b0b8"/><stop offset="1" stop-color="#6a7680"/>
      </linearGradient>
    </defs>
    <rect width="380" height="537" fill="var(--white)"/>
    <g role="img" aria-label="Aerial photo of a factory roof covered in solar panels">
      <path d="M60 60 Q200 20 380 30 L380 270 L0 270 L0 140 Z" fill="url(#roofTop)"/>
    </g>
    <g role="img" aria-label="Aerial photo of an industrial site with rooftop solar and a car park">
      <path d="M0 330 L380 330 L380 537 L0 537 Z" fill="url(#roofLow)"/>
    </g>
    <path d="M0 0 L380 0 L380 30 Q200 18 60 60 Q20 80 0 140 Z" fill="var(--navy)"/>
    <path d="M0 150 Q20 80 70 62 Q30 90 12 160 Z" fill="var(--sky)"/>
    <path d="M380 400 Q330 490 230 537 L380 537 Z" fill="var(--navy)"/>
    <path d="M380 440 Q350 500 300 537 L380 537 Z" fill="var(--sky)"/>
  </svg>
  <div class="price-badge badge-30">Less then 30kW<span class="big">$30<small> Ex.</small></span>Gst Skyplan<br>Panel Layout</div>
  <div class="tier tier-mid">31kW - 100kW<br>$80 Ex. Gst Skyplan<br>Panel Layout</div>
  <div class="service-head">
    <h2>Services – Professional Panel Layout</h2>
    <p>We can layout the panels for a small fee<br>Clear &amp; Concise<br>Ranging from 5kW – 300kW</p>
  </div>
  <div class="tier tier-large">101kW - 300kW<br>$150 Ex. Gst Skyplan<br>Panel Layout</div>
  <div class="price-badge badge-3d"><span>300kW+</span><span>$360 Ex.Gst</span><span><span class="big">3D</span> Drawings</span><span>including shading</span><span>analysis</span></div>
</section>

<section class="page spread-right">
  <svg class="bg" viewBox="0 0 380 537" preserveAspectRatio="none">
    <defs>
      <linearGradient id="panelMist" x1="0" y1="0" x2="1" y2="1">
        <stop offset="0" stop-color="#dde6f0"/><stop offset="1" stop-color="#a9bdd4"/>
      </linearGradient>
    </defs>
    <g role="img" aria-label="Faded close-up photo of solar panel cells">
      <rect width="380" height="537" fill="url(#panelMist)"/>
    </g>
    <path d="M0 0 L380 0 L380 28 Q160 50 0 250 Z" fill="var(--navy)"/>
    <path d="M110 115 Q230 40 380 28 L380 100 Q250 105 150 130 Z" fill="var(--sky)"/>
    <path d="M380 370 Q340 490 210 537 L380 537 Z" fill="var(--navy)"/>
  </svg>
  <h2 class="grid-title">Grid Connection<br>Services<br>30kW – 150kW</h2>

  <div class="rate-card card-a">
    <h3>Coralgrid, Unity Networks</h3>
    <table>
      <tr><th>Service</th><th></th><th class="rate">Rates</th></tr>
      <tr><td rowspan="5">Network Application &amp; Case Management</td><td>AC schematic</td><td class="rate" rowspan="5">$670</td></tr>
      <tr><td>Site plan</td></tr>
      <tr><td>Voltage rise study</td></tr>
      <tr><td>Completed paperwork</td></tr>
      <tr><td>Case Management to approval</td></tr>
    </table>
  </div>

  <div class="rate-card card-b">
    <h3>Southnet, Harbourgrid</h3>
    <table>
      <tr><th>Service</th><th></th><th class="rate">Rates</th></tr>
      <tr><td rowspan="5">Network Application &amp; Case Management</td><td>AC schematic</td><td class="rate" rowspan="5">$980</td></tr>
      <tr><td>Site plan</td></tr>
      <tr><td>Voltage rise study</td></tr>
      <tr><td>Completed paperwork</td></tr>
      <tr><td>Case Management to approval</td></tr>
      <tr><td>Onsite Commissioning</td><td>Injection testing &amp; report</td><td class="rate">$1350</td></tr>
    </table>
  </div>

  <div class="rate-card card-c">
    <h3>Kestrel Networks</h3>
    <table>
      <tr><th>Service</th><th></th><th class="rate">Rates</th></tr>
      <tr><td rowspan="8">Network Application &amp; Case Management</td><td>AC schematic</td><td class="rate" rowspan="8">$980</td></tr>
      <tr><td>PV yield &amp; load profile study</td></tr>
      <tr><td>Site plan</td></tr>
      <tr><td>Voltage rise study</td></tr>
      <tr><td>Protection grading study</td></tr>
      <tr><td>Technical report</td></tr>
      <tr><td>Completed paperwork</td></tr>
      <tr><td>Case Management to approval</td></tr>
      <tr><td>Onsite Commissioning</td><td>Injection testing &amp; report</td><td class="rate">$1350</td></tr>
    </table>
  </div>
</section>

</body>
</html>
```